Varemo - Nutritious Snacks and Desserts

We need a creative e-commerce website in which all features--buttons, background, etc.--convey our message: We sell delicious, nutritious snacks and desserts that most closely comply with the paleo diet guidelines. Our first product is Brantoza®--raw, vegan, paleo chocolate balls that are made of dates, coconut, and cocoa. Our products are organic, raw, irresistible and nutritious. We have several versions of Brantoza® in development, as well as mousse, ice cream, and crackers. Our mission is to purvey basic healthy foods. Our motto is, "Fuel for the Daring Trail-Seeker(tm)."

Target Market(s)

Health-conscious professionals who tend to shop at health food stores. Our products also meet the requirements of a gluten-free diet; and they also don't contain refined sugar, so shoppers with gluten and possibly sugar issues are incidental customers.

Industry/Entity Type

Health Product

Coding

Coded - Design and coding required

Number of Pages Required

5+ page

Colors

Designer to choose colors to be used in the design.

Requirements
Must have
• We need at least a home page, a products page, an about-us page, a contact page, and a shopping cart page. We would like to be able to add products on our own later. We should be able to handle some basic coding, especially if it's just a matter of copying and modifying product pages. We would also like the ability in the future to add blogging pages, allowing us to write articles about health food and healthy lifestyle, thus attracting web-traffic (SEO).
• Other features we would like to have:
• Product photo slider on the hopepage
• Back-to-top button at the bottom of the home page
• Make sure the site is mobile-compatible
• A search bar at the top of the homepage
• "Create an account" and "Previous orders"--allowing customers to see their previous orders and reorder what they purchased in the past.
Nice to have
• We would like to convey the paleo theme without actually stating it anywhere. We'll add text as necessary, according to the page layout; you can use ipsum lorem for purpose of demonstration.

```html
<!DOCTYPE html>
<html lang="en">
<head>
<meta charset="utf-8">
<title>Varemo Foods – Nutritious Snacks and Desserts</title>
<link rel="stylesheet" href="https://fonts.googleapis.com/css2?family=Montserrat:wght@400;500;600;700&family=Permanent+Marker&family=Amatic+SC:wght@700&family=Yellowtail&display=swap">
<style>
:root{
  --green:#5a9a12;
  --green-dark:#4a8410;
  --green-light:#7bbf24;
  --ink:#222;
  --grey-text:#555;
  --muted:#777;
  --paper:#fff;
  --wash:#eff0ed;
  --line:#d8d8d8;
  --hero-dark:#231f1b;
  --wood:#3b2416;
}
*{box-sizing:border-box;margin:0;padding:0}
html,body{width:1200px;height:3409px;overflow:hidden}
body{position:relative;font-family:"Montserrat",Arial,sans-serif;color:var(--ink);background:var(--paper)}
.abs{position:absolute}
.brand{display:flex;flex-direction:column;align-items:center;gap:6px}
.brand-dot{width:64px;height:64px;border-radius:50%;background:var(--green)}
.brand-name{font-family:"Montserrat",sans-serif;font-weight:700;color:var(--green);font-size:32px;letter-spacing:3px}

/* top bar */
.topbar{left:0;top:0;width:1200px;height:23px;background:var(--green-dark);color:#fff;font-size:11px;display:flex;align-items:center}
.topbar .contact{position:absolute;left:118px;display:flex;align-items:center;gap:8px}
.topbar .phone{left:420px}
.topbar .sep{position:absolute;left:392px;top:5px;width:1px;height:13px;background:rgba(255,255,255,.7)}
.topbar .socials{position:absolute;right:118px;display:flex;gap:7px}
.dot-ico{width:13px;height:13px;border-radius:50%;background:#fff}

/* header */
.header{left:0;top:23px;width:1200px;height:141px;border-bottom:1px solid #eee}
.search{left:118px;top:57px;width:200px;height:34px;border:1px solid #ccc;font-size:11px;color:#555;padding:0 10px;display:flex;align-items:center;justify-content:space-between}
.header .brand{left:500px;top:15px;width:200px}
.header-icons{left:990px;top:58px;display:flex;gap:20px;align-items:center}
.cart-badge{position:absolute;left:50px;top:-6px;width:14px;height:14px;border-radius:50%;background:var(--green);color:#fff;font-size:9px;text-align:center;line-height:14px}
.nav{left:0;top:164px;width:1200px;height:46px;border-bottom:1px solid #eee;display:flex;justify-content:center;align-items:center;gap:60px;font-size:13px;font-weight:500}
.nav .bullet{width:5px;height:5px;border-radius:50%;background:var(--green)}

/* hero */
.hero{left:0;top:211px;width:1200px;height:596px;background:radial-gradient(ellipse at 60% 40%,#5a4a3c 0%,#2e2721 55%,var(--hero-dark) 100%)}
.hero-title{left:0;width:1200px;text-align:center;font-family:"Permanent Marker",cursive;font-size:82px;line-height:1}
.hero-title.white{top:150px;color:#fff}
.hero-title.green{top:240px;color:var(--green-light)}
.hero-sub{left:0;top:345px;width:1200px;text-align:center;color:#fff;font-size:22px}
.btn{display:flex;align-items:center;justify-content:center;gap:10px;background:var(--green);color:#fff;font-size:12px;font-weight:600;text-transform:uppercase}
.hero .btn{left:518px;top:398px;width:166px;height:43px}
.slide-nums{left:1128px;top:205px;width:72px;font-size:13px;color:#fff}
.slide-nums div{height:26px;border-bottom:1px solid rgba(255,255,255,.35);padding-left:0}
.slide-nums .on{color:var(--green-light)}
.hero-dots{left:594px;top:534px;display:flex;flex-direction:column;gap:10px}
.hero-dots span{width:8px;height:8px;border-radius:50%;background:#fff}
.hero-dots .on{background:var(--green-light)}

/* intro */
.intro{left:0;top:807px;width:1200px;height:632px;background:var(--wash)}
.intro-title{left:95px;top:140px;font-family:"Amatic SC",cursive;font-weight:700;font-size:58px;color:var(--green);line-height:1}
.intro-sub{left:95px;top:210px;font-size:20px;color:var(--ink)}
.intro-rule{left:95px;top:255px;width:110px;height:2px;background:#ccc}
.intro-text{left:95px;top:278px;width:432px;font-size:12.5px;line-height:17px;color:var(--grey-text);text-align:justify}
.intro .btn{left:95px;top:466px;width:166px;height:41px}
.intro-photo{left:573px;top:125px;width:527px;height:393px;background:linear-gradient(135deg,#b7b7b5,#9a9a98 60%,#8a8a88)}

/* products */
.products-band{left:0;top:1439px;width:1200px;height:316px;background:linear-gradient(180deg,var(--green-dark),var(--green))}
.script{font-family:"Yellowtail",cursive;color:var(--green-light);font-size:38px;text-align:center;width:1200px;left:0;line-height:1}
.section-title{left:0;width:1200px;text-align:center;font-size:40px;font-weight:600;letter-spacing:1px;line-height:1}
.notch{left:575px;top:1600px}
.product-card{left:98px;top:1636px;width:1004px;height:569px;background:#fff;box-shadow:0 6px 20px rgba(0,0,0,.08)}
.product-photo{left:111px;top:84px;width:421px;height:417px;background:linear-gradient(160deg,#8a8b86,#c9c3b4 45%,#8e6b47 80%)}
.deal{left:560px;top:70px;width:376px;text-align:center}
.deal .daily{font-family:"Yellowtail",cursive;color:var(--green);font-size:36px;line-height:1}
.deal .deals{font-size:38px;font-weight:600;color:#666;line-height:1}
.deal .name{font-size:22px;font-weight:700;margin-top:34px}
.deal .stars{color:var(--green);font-size:18px;letter-spacing:2px;margin-top:8px}
.deal .price{color:var(--green);font-size:24px;font-weight:700;margin-top:2px}
.deal .desc{font-size:12px;line-height:16px;color:var(--grey-text);width:250px;margin:20px auto 0}
.deal .btn{margin:32px auto 0;width:164px;height:41px}
.arrow-box{width:59px;height:59px;background:#c9c9c9;display:flex;align-items:center;justify-content:center}

/* blog */
.blog-title{top:2264px;color:#666}
.blog-rule{left:570px;top:2305px;width:60px;height:3px;background:var(--green)}
.post{top:2337px;width:300px;height:450px;background:#fff;border:1px solid var(--line);box-shadow:0 2px 6px rgba(0,0,0,.06)}
.post .date{position:absolute;right:14px;top:16px;font-size:10px;color:#555}
.post .photo{position:absolute;left:0;top:43px;width:300px;height:157px;background:linear-gradient(135deg,#3d3a34,#8a7f68 45%,#5d2f3a 75%,#2f3d22)}
.post .ptitle{position:absolute;left:16px;top:224px;font-size:12px;font-weight:700;color:var(--green);letter-spacing:.5px}
.post .pcat{position:absolute;left:16px;top:244px;font-size:10px;color:#777}
.post .pbody{position:absolute;left:16px;top:290px;width:260px;font-size:11.5px;line-height:17px;color:#555}
.post .more{position:absolute;left:16px;top:392px;width:116px;height:34px;border:1px solid var(--green);color:var(--green);font-size:10px;font-weight:600;display:flex;align-items:center;justify-content:center}
.post .share{position:absolute;right:14px;top:400px;display:flex;gap:4px}
.post .share span{width:19px;height:19px;border-radius:50%;background:var(--green)}
.pager{left:528px;top:2831px;display:flex;gap:10px}
.pager span{width:40px;height:3px;background:#ccc}
.pager .on{background:#999}

/* footer */
.footer-scene{left:0;top:2869px;width:1200px;height:472px;background:linear-gradient(90deg,#2a1a10,var(--wood) 30%,#4a2e1c 70%,#2a1a10)}
.footer-tab{left:570px;top:2862px;width:60px;height:22px;background:#fff;border-radius:0 0 30px 30px}
.footer-panel{left:375px;top:3000px;width:432px;height:269px;background:rgba(25,22,20,.85)}
.footer-logo{left:521px;top:2996px;width:158px;height:158px;border-radius:50%;background:#fff;display:flex;align-items:center;justify-content:center}
.footer-logo .brand-dot{width:48px;height:48px}
.footer-logo .brand-name{font-size:26px}
.footer-motto{left:375px;top:3165px;width:432px;text-align:center;color:#fff;font-size:19px;font-weight:500;line-height:25px;text-transform:uppercase}
.contact-btn{left:395px;top:3289px;width:400px;height:52px;background:#fff;color:var(--green);font-size:19px;font-weight:700;display:flex;align-items:center;justify-content:center}
.bottombar{left:0;top:3341px;width:1200px;height:68px;background:var(--green-dark);color:#fff;font-size:11px;display:flex;align-items:center}
.bottombar .copy{position:absolute;left:118px}
.bottombar .socials{position:absolute;right:118px;display:flex;gap:22px}
</style>
</head>
<body>

<div class="abs topbar">
  <div class="contact">
    <svg width="13" height="13" viewBox="0 0 13 13"><circle cx="6.5" cy="6.5" r="6.5" fill="#fff"/><rect x="3" y="4" width="7" height="5" fill="none" stroke="#4a8410" stroke-width="1"/><path d="M3 4l3.5 3 3.5-3" fill="none" stroke="#4a8410" stroke-width="1"/></svg>
    Email us at hello@varemo-mail.com
  </div>
  <span class="sep"></span>
  <div class="contact phone">
    <svg width="13" height="13" viewBox="0 0 13 13"><circle cx="6.5" cy="6.5" r="6.5" fill="#fff"/><path d="M4.3 3.5l1.3 1.4-.7 1c.4.9 1 1.5 1.9 1.9l1-.7 1.4 1.3-.8 1c-2.6-.3-4.8-2.5-5.1-5.1z" fill="#4a8410"/></svg>
    (555) 010 - 2040
  </div>
  <div class="socials"><span class="dot-ico"></span><span class="dot-ico"></span><span class="dot-ico"></span><span class="dot-ico"></span></div>
</div>

<header class="abs header">
  <div class="abs search">SEARCH
    <svg width="12" height="12" viewBox="0 0 12 12"><circle cx="5" cy="5" r="3.8" fill="none" stroke="#333" stroke-width="1.5"/><path d="M8 8l3 3" stroke="#333" stroke-width="1.5"/></svg>
  </div>
  <div class="abs brand"><span class="brand-dot"></span><span class="brand-name">varemo</span></div>
  <div class="abs header-icons">
    <svg width="26" height="26" viewBox="0 0 26 26"><circle cx="13" cy="13" r="12" fill="none" stroke="#555" stroke-width="1.5"/><circle cx="13" cy="10" r="4" fill="none" stroke="#555" stroke-width="1.5"/><path d="M6 21c2-4 12-4 14 0" fill="none" stroke="#555" stroke-width="1.5"/></svg>
    <svg width="26" height="26" viewBox="0 0 26 26"><path d="M4 8h18l-2 14H6z" fill="none" stroke="#555" stroke-width="1.5"/><path d="M9 8V6a4 4 0 0 1 8 0v2" fill="none" stroke="#555" stroke-width="1.5"/></svg>
    <span class="cart-badge">0</span>
  </div>
</header>

<nav class="abs nav">
  <span>HOME</span><span class="bullet"></span>
  <span>ABOUT US</span><span class="bullet"></span>
  <span>PRODUCTS</span><span class="bullet"></span>
  <span>BLOG</span><span class="bullet"></span>
  <span>CONTACT US</span>
</nav>

<section class="abs hero" role="img" aria-label="Dark table with a plated seafood and noodle dish">
  <h1 class="abs hero-title white">WELCOME TO</h1>
  <h1 class="abs hero-title green">VAREMO FOODS.</h1>
  <p class="abs hero-sub">Fuel for the Daring Trail-SeekerTM</p>
  <a class="abs btn">Get Started</a>
  <div class="abs slide-nums"><div class="on">01</div><div>02</div><div>03</div><div>04</div></div>
  <div class="abs hero-dots"><span class="on"></span><span></span></div>
</section>

<section class="abs intro">
  <h2 class="abs intro-title">WELCOME TO VAREMO FOODS.</h2>
  <p class="abs intro-sub">Fuel for the Daring Trail-SeekerTM</p>
  <span class="abs intro-rule"></span>
  <p class="abs intro-text">Lorem Ipsum is simply dummy text of the printing and typesetting industry. Lorem Ipsum has been the industry's standard dummy text ever since the 1500s, when an unknown printer took a galley of type and scrambled it to make a type specimen book. It has survived not only five centuries, but also the leap into electronic typesetting, remaining essentially unchanged. It was popularised in the 1960s with the release of Letraset sheets containing Lorem Ipsum passages.</p>
  <a class="abs btn">Read More
    <svg width="12" height="10" viewBox="0 0 12 10"><path d="M0 5h10M6 1l4 4-4 4" fill="none" stroke="#fff" stroke-width="1.5"/></svg>
  </a>
  <div class="abs intro-photo" role="img" aria-label="Person holding up a white sign with the brand name"></div>
</section>

<section class="abs products-band">
  <p class="abs script" style="top:58px">My Popular</p>
  <h2 class="abs section-title" style="top:96px;color:#fff">PRODUCTS</h2>
</section>
<svg class="abs notch" width="50" height="22" viewBox="0 0 50 22"><path d="M0 0h50L25 20z" fill="#fff"/></svg>

<div class="abs product-card">
  <div class="abs product-photo" role="img" aria-label="Paper tub of Brantoza chocolate balls"></div>
  <div class="abs deal">
    <p class="daily">Daily</p>
    <p class="deals">DEALS</p>
    <svg width="60" height="8" viewBox="0 0 60 8" style="margin-top:8px"><path d="M0 4h24M36 4h24" stroke="#bbb"/><circle cx="30" cy="4" r="3" fill="none" stroke="#bbb"/></svg>
    <p class="name" style="margin-top:26px">BRANTOZA®</p>
    <p class="stars">★★★★★</p>
    <p class="price">$80.00</p>
    <p class="desc">Our products are raw, organic, vegan, gluten-free, dairy-free, fiber-rich, nutrient-dense, antioxidant-rich real foods with no preservatives, no added sugar, and no artificial or plant-based sweeteners. And they are irresistibly scrumptious!</p>
    <a class="btn">Add to Cart
      <svg width="14" height="14" viewBox="0 0 14 14"><path d="M2 4h10l-1 9H3z" fill="none" stroke="#fff" stroke-width="1.3"/><path d="M5 4V3a2 2 0 0 1 4 0v1" fill="none" stroke="#fff" stroke-width="1.3"/></svg>
    </a>
  </div>
</div>
<div class="abs arrow-box" style="left:98px;top:1875px"><svg width="16" height="28" viewBox="0 0 16 28"><path d="M14 2L2 14l12 12" fill="none" stroke="#fff" stroke-width="2"/></svg></div>
<div class="abs arrow-box" style="left:1043px;top:1875px"><svg width="16" height="28" viewBox="0 0 16 28"><path d="M2 2l12 12L2 26" fill="none" stroke="#fff" stroke-width="2"/></svg></div>

<p class="abs script" style="top:2212px;color:var(--green)">Latest from</p>
<h2 class="abs section-title blog-title">THE BLOG</h2>
<span class="abs blog-rule"></span>

<article class="abs post" style="left:118px">
  <span class="date">MAY 10, 2018, WEDNESDAY</span>
  <div class="photo" role="img" aria-label="Plate of salad with flatbread"></div>
  <h3 class="ptitle">LOREM IPSUM DOLOR SIT AMET</h3>
  <p class="pcat">FOOD / PORTFOLIO</p>
  <p class="pbody">Lorem ipsum dolor sit amet, consectetur adipiscing elit. Sed euismod in tellus in mattis. Aliquam erat volutpat. Praesent ultricies aliquet erat a semper.</p>
  <a class="more">READ MORE</a>
  <div class="share"><span></span><span></span><span></span><span></span></div>
</article>
<article class="abs post" style="left:448px">
  <span class="date">MAY 10, 2018, WEDNESDAY</span>
  <div class="photo" role="img" aria-label="Plate of salad with flatbread"></div>
  <h3 class="ptitle">LOREM IPSUM DOLOR SIT AMET</h3>
  <p class="pcat">FOOD / PORTFOLIO</p>
  <p class="pbody">Lorem ipsum dolor sit amet, consectetur adipiscing elit. Sed euismod in tellus in mattis. Aliquam erat volutpat. Praesent ultricies aliquet erat a semper.</p>
  <a class="more">READ MORE</a>
  <div class="share"><span></span><span></span><span></span><span></span></div>
</article>
<article class="abs post" style="left:780px">
  <span class="date">MAY 10, 2018, WEDNESDAY</span>
  <div class="photo" role="img" aria-label="Plate of salad with flatbread"></div>
  <h3 class="ptitle">LOREM IPSUM DOLOR SIT AMET</h3>
  <p class="pcat">FOOD / PORTFOLIO</p>
  <p class="pbody">Lorem ipsum dolor sit amet, consectetur adipiscing elit. Sed euismod in tellus in mattis. Aliquam erat volutpat. Praesent ultricies aliquet erat a semper.</p>
  <a class="more">READ MORE</a>
  <div class="share"><span></span><span></span><span></span><span></span></div>
</article>
<div class="abs pager"><span class="on"></span><span></span><span></span></div>

<section class="abs footer-scene" role="img" aria-label="Wooden table with salad, pasta, tomatoes and herbs"></section>
<div class="abs footer-tab"></div>
<svg class="abs" style="left:590px;top:2866px" width="20" height="12" viewBox="0 0 20 12"><path d="M3 2l7 7 7-7" fill="none" stroke="var(--green)" stroke-width="2.5"/></svg>
<div class="abs footer-panel"></div>
<div class="abs footer-logo"><div class="brand"><span class="brand-dot"></span><span class="brand-name">varemo</span></div></div>
<p class="abs footer-motto">Fuel for the Daring<br>Trail-SeekerTM</p>
<a class="abs contact-btn">CONTACT US</a>

<footer class="abs bottombar">
  <span class="copy">© 2018 Varemo Foods . All Right Reserved.</span>
  <div class="socials"><span class="dot-ico" style="width:10px;height:10px"></span><span class="dot-ico" style="width:10px;height:10px"></span><span class="dot-ico" style="width:10px;height:10px"></span><span class="dot-ico" style="width:10px;height:10px"></span></div>
</footer>

</body>
</html>
```